DL flyer front and back + magnet

DL Flyer Design Brief – VKD Plumbing

Objective:
Create a bold, high-impact DL flyer promoting a Blocked Drain Special to generate immediate service calls.

Main Headline (Large & Eye Catching)

🚨 BLOCKED DRAIN SPECIAL – $299 🚨

High Pressure Water Jetting

Offer Details

💧 Clear stubborn blocked drains fast
💧 Professional high-pressure water jetting
💧 Removes tree roots, grease & debris

Limited Time Bonus

⭐ FIRST 15 CALLS RECEIVE A FREE CCTV CAMERA INSPECTION
(Valued at $149)

Trust Points (Icons or Ticks)

✔ Local Licensed Plumbers
✔ Fast Same Day Service
✔ Upfront Pricing
✔ 5 Star Rated Service

Call To Action (Very Prominent)

📞 CALL NOW TO BOOK
Limited bookings available

Phone: 0491 570 006
Website: vkdplumbing.com.au

Branding

Include:

VKD Plumbing logo

Plumbing imagery (blocked drain / jetting hose)

Use brand colours from VKD logo
💡 Design Tip:
The $299 price should be the biggest element on the flyer so people instantly see the offer.

Back Side Layout – VKD Plumbing Flyer
🏠 Your Local Trusted Plumber

Fast, Reliable Plumbing Services Across the Sutherland Shire

We provide professional plumbing services for homes and businesses including:

Our Services

✔ Blocked Drains
✔ Leak Detection & Repairs
✔ Hot Water Systems
✔ Tap & Toilet Repairs
✔ Stormwater Repairs
✔ CCTV Drain Inspections
✔ Gutter & Roof Plumbing
✔ Preventative Plumbing Maintenance

⭐ Why Choose VKD Plumbing?

✔ Fully Licensed & Insured
✔ Upfront Honest Pricing
✔ Fast Local Service
✔ Clean & Professional Workmanship
✔ Trusted by Local Homeowners & Businesses

⭐ What Our Customers Say

⭐⭐⭐⭐⭐
"Lachlan from VKD Plumbing cleared our blocked drain quickly and professionally. Highly recommend!"

⭐⭐⭐⭐⭐
"Prompt, reliable and great service. Will definitely use again."

(Fintaro Ratings)

📞 Need a Plumber?

VKD Plumbing

📞 Call: 0491 570 006
🌐 vkdplumbing.com.au

Add this small section on the back:

Neighbour Discount

💧 $59 OFF ANY PLUMBING REPAIR
(Mention this flyer when booking)

Magnet should be similar to these

```html
<!DOCTYPE html>
<html lang="en">
<head>
<meta charset="utf-8">
<title>VKD Plumbing – DL Flyer and Magnet</title>
<link rel="stylesheet" href="https://fonts.googleapis.com/css2?family=Signika:wght@300;400;600;700&display=swap">
<style>
:root{
  --cyan:#29bde6;
  --blue:#1a75bb;
  --navy:#1f5aa8;
  --yellow:#f6bf3c;
  --white:#ffffff;
  --backdrop:#ece8e3;
  --drain-dark:#4a3424;
  --drain-mid:#8a6a48;
}
*{margin:0;padding:0;box-sizing:border-box}
html,body{width:1200px;height:960px;overflow:hidden}
body{background:var(--backdrop);font-family:"Signika",sans-serif;color:var(--white);position:relative}
.panel{position:absolute;overflow:hidden;box-shadow:0 2px 8px rgba(0,0,0,.18)}
.abs{position:absolute}
svg.abs{overflow:visible}

/* ---------- Front ---------- */
.flyer-front{left:55px;top:47px;width:359px;height:757px;background:var(--cyan)}
.front-top-white{left:0;top:0}
.brand{left:22px;top:52px;color:var(--blue);font-weight:700;line-height:.9;display:flex;align-items:center;gap:6px}
.brand-name{font-size:50px;letter-spacing:1px}
.brand-sub{display:block;font-size:17px;letter-spacing:2.5px;margin-top:4px}
.brand-dot{width:12px;height:12px;border-radius:50%;background:var(--yellow);align-self:flex-start;margin-top:6px}
.headline{right:22px;top:22px;text-align:right;font-weight:700;line-height:.95;text-transform:uppercase}
.headline .l1{font-size:30px;display:block}
.headline .l2{font-size:42px;display:block}
.headline .l3{font-size:32px;display:block}
.drain-photo{left:0;top:139px;width:359px;height:229px;background:radial-gradient(ellipse at 70% 45%,var(--drain-mid) 0%,var(--drain-dark) 55%,#2a1e14 100%)}
.price-box{left:202px;top:124px;width:144px;height:57px;background:var(--yellow);font-weight:700;font-size:54px;line-height:57px;text-align:center;z-index:2}
.offer-bars{left:0;top:292px;width:359px}
.offer-bar{position:relative;height:17px;margin-bottom:6px;margin-left:100px;font-size:11.5px;font-weight:700;line-height:17px;padding-left:16px}
.offer-bar::before{content:"";position:absolute;inset:0 2px 0 -8px;background:var(--blue);transform:skewX(-35deg);z-index:-1}
.offer-bar{z-index:1}
.drop{display:inline-block;width:6px;height:8px;background:var(--cyan);border-radius:50% 50% 50% 50%/60% 60% 40% 40%;margin-right:5px}
.bonus-label{left:0;width:359px;top:370px;text-align:center;font-size:10.5px;font-weight:300}
.bonus-text{left:8px;width:206px;top:412px;text-align:center;font-weight:700;font-size:12.8px;line-height:16px;text-transform:uppercase}
.bonus-text .value{font-size:13.5px;text-transform:none;display:block;margin-top:1px}
.stars{color:var(--yellow);letter-spacing:9px;font-size:13px}
.bonus-stars{left:62px;top:465px}
.trust-list{left:26px;top:489px;list-style:none;font-weight:700;font-size:11.5px}
.trust-list li{height:23px;display:flex;align-items:center;gap:5px}
.tick{width:11px;height:9px}
.cta{left:37px;top:608px;font-weight:700;font-size:20px;line-height:19px;text-transform:uppercase;text-align:center}
.cta span{display:block;background:var(--yellow);padding:0 8px}
.cta .b{margin:0 auto;width:86px;padding:0}
.cta-note{left:38px;top:656px;font-size:10.5px;font-weight:600}
.front-contact{left:20px;top:684px}
.front-phone{font-size:20px;font-weight:700;margin-left:28px;line-height:20px}
.front-web{font-size:12.5px;font-weight:700;margin-left:28px;margin-top:2px}
.front-contact svg{position:absolute;left:0;top:0}
.person-front{left:160px;top:390px;width:199px;height:367px;background:linear-gradient(180deg,#c99f7e 0%,#c99f7e 22%,#1d2a45 30%,#1d2a45 100%);border-radius:90px 90px 0 0;opacity:.92}

/* ---------- Back ---------- */
.flyer-back{left:437px;top:50px;width:356px;height:754px;background:var(--cyan)}
.back-title{left:23px;top:16px;font-size:23.5px;font-weight:600}
.back-check{left:48px;top:62px}
.back-sub{left:97px;top:58px;font-size:14px;font-weight:600;line-height:18px}
.back-intro{left:28px;top:108px;font-size:11.5px;line-height:16px;font-weight:600}
.tag{background:var(--yellow);font-size:11.5px;font-weight:600;height:19px;line-height:19px;padding:0 12px}
.services-tag{left:24px;top:147px;width:104px}
.why-tag{left:69px;top:322px;width:191px;text-align:center}
.tri-list{list-style:none;font-size:11.8px;font-weight:600}
.tri-list li{height:16.6px;display:flex;align-items:center;gap:6px}
.tri{width:0;height:0;border-left:6px solid var(--yellow);border-top:4px solid transparent;border-bottom:4px solid transparent}
.services-list{left:30px;top:177px}
.why-list{left:70px;top:352px}
.why-list li{height:16.7px}
.reviews-band{left:0;top:451px;width:356px;height:171px;background:var(--yellow)}
.reviews-tab{left:0;top:468px}
.reviews-tab-text{left:58px;top:471px;font-size:11.5px;font-weight:600}
.rating-source{left:272px;top:463px;text-align:center;line-height:1}
.rating-source .name{font-size:15px;font-weight:600}
.rating-source .sub{font-size:5.5px;display:block;margin-top:2px}
.quotes{left:0;width:356px;top:496px;text-align:center;color:var(--navy);font-weight:600;font-size:11.8px;line-height:16px}
.quotes .stars{color:var(--navy);letter-spacing:8px;font-size:12px;display:block;margin:0 0 4px 8px}
.quotes p{margin-bottom:4px}
.contact-band{left:0;top:622px;width:356px;height:83px;background:var(--blue);text-align:center;font-weight:700}
.need{color:var(--yellow);font-size:23px;line-height:24px;margin-top:8px}
.call{font-size:28px;line-height:28px}
.call .word{color:var(--yellow);font-size:23px}
.web{font-size:17px;line-height:20px}
.contact-band .phone-icon{position:absolute;left:55px;top:39px}
.contact-band .pointer{position:absolute;left:88px;top:65px}
.discount{left:0;width:356px;top:716px;text-align:center;font-weight:700;font-size:12.8px;line-height:14px}

/* ---------- Magnet ---------- */
.magnet{left:823px;top:59px;width:324px;height:231px;border-radius:22px;background:var(--blue)}
.magnet-shapes{left:0;top:0}
.mag-need{left:20px;top:17px;font-weight:700;line-height:1}
.mag-need .q{color:var(--yellow);font-size:15.5px;display:block}
.mag-need .call{font-size:19px;line-height:20px}
.mag-need .call .word{font-size:15.5px}
.mag-need .web{font-size:12.5px;line-height:16px;display:block;margin-left:11px}
.mag-tag{left:189px;top:19px;width:85px;height:15px;background:var(--yellow);color:var(--blue);font-size:9px;font-weight:700;text-align:center;line-height:15px}
.mag-list{left:194px;top:41px;font-size:8.8px}
.mag-list li{height:13.6px;gap:4px}
.mag-list .tri{border-left-width:4px;border-top-width:3px;border-bottom-width:3px}
.mag-list li.two{height:auto;line-height:9.5px;align-items:flex-start}
.mag-list li.two .tri{margin-top:2px}
.mag-brand{left:14px;top:166px;color:var(--blue);font-weight:700;line-height:.9}
.mag-brand .brand-name{font-size:38px}
.mag-brand .brand-sub{font-size:12.5px;letter-spacing:2px;margin-top:2px}
.person-magnet{left:110px;top:103px;width:69px;height:128px;background:linear-gradient(180deg,#c99f7e 0%,#c99f7e 22%,#1d2a45 30%,#1d2a45 100%);border-radius:32px 32px 0 0;opacity:.92}
</style>
</head>
<body>

<!-- Front of DL flyer -->
<section class="panel flyer-front" aria-label="Flyer front">
  <svg class="abs front-top-white" width="359" height="140" viewBox="0 0 359 140">
    <path d="M0,5 Q120,0 175,45 Q205,80 218,139 L0,139 Z" fill="#ffffff"/>
  </svg>
  <div class="abs brand"><div><span class="brand-name">VKD</span><span class="brand-sub">PLUMBING</span></div><span class="brand-dot"></span></div>
  <h1 class="abs headline"><span class="l1">Blocked</span><span class="l2">Drain</span><span class="l3">Special</span></h1>
  <div class="abs drain-photo" role="img" aria-label="Photo of a high-pressure jetting hose spraying water inside a dirty drain pipe"></div>
  <div class="abs price-box">$299</div>
  <div class="abs offer-bars">
    <div class="offer-bar"><span class="drop"></span>Clear stubborn blocked drains fast</div>
    <div class="offer-bar"><span class="drop"></span>Professional high-pressure water jetting</div>
    <div class="offer-bar"><span class="drop"></span>Removes tree roots, grease &amp; debris</div>
  </div>
  <div class="abs bonus-label">Limited Time Bonus</div>
  <div class="abs person-front" role="img" aria-label="Photo of the plumber Lachlan in a navy polo shirt, arms crossed"></div>
  <p class="abs bonus-text">First 15 calls receive a free CCTV camera inspection<span class="value">(Valued at $149)</span></p>
  <div class="abs stars bonus-stars">★★★★★</div>
  <ul class="abs trust-list">
    <li><svg class="tick" viewBox="0 0 11 9"><path d="M1,5 L4,8 L10,1" stroke="#f6bf3c" stroke-width="2.2" fill="none"/></svg>Local Licensed Plumbers</li>
    <li><svg class="tick" viewBox="0 0 11 9"><path d="M1,5 L4,8 L10,1" stroke="#f6bf3c" stroke-width="2.2" fill="none"/></svg>Fast Same Day Service</li>
    <li><svg class="tick" viewBox="0 0 11 9"><path d="M1,5 L4,8 L10,1" stroke="#f6bf3c" stroke-width="2.2" fill="none"/></svg>Upfront Pricing</li>
    <li><svg class="tick" viewBox="0 0 11 9"><path d="M1,5 L4,8 L10,1" stroke="#f6bf3c" stroke-width="2.2" fill="none"/></svg>5 Star Rated Service</li>
  </ul>
  <div class="abs cta"><span class="a">Call Now</span><span class="b">To Book</span></div>
  <div class="abs cta-note">Limited bookings available</div>
  <div class="abs front-contact">
    <svg width="26" height="34" viewBox="0 0 26 34">
      <rect x="2" y="2" width="12" height="20" rx="3" fill="#1a75bb"/>
      <rect x="4.5" y="5" width="7" height="6" fill="#29bde6"/>
      <path d="M16,18 L16,30 L19,27 L22,32 L24,31 L21,26 L25,26 Z" fill="#f6bf3c"/>
    </svg>
    <div class="front-phone">0491 570 006</div>
    <div class="front-web">vkdplumbing.com.au</div>
  </div>
</section>

<!-- Back of DL flyer -->
<section class="panel flyer-back" aria-label="Flyer back">
  <h2 class="abs back-title">Your Local Trusted Plumber</h2>
  <svg class="abs back-check" width="34" height="26" viewBox="0 0 34 26"><path d="M3,13 L12,22 L31,3" stroke="#f6bf3c" stroke-width="6" fill="none"/></svg>
  <p class="abs back-sub">Fast, Reliable Plumbing Services<br>Across the Sutherland Shire</p>
  <p class="abs back-intro">We provide professional plumbing services<br>for homes and businesses including:</p>
  <div class="abs tag services-tag">OUR SERVICES</div>
  <ul class="abs tri-list services-list">
    <li><span class="tri"></span>Blocked Drains</li>
    <li><span class="tri"></span>Leak Detection &amp; Repairs</li>
    <li><span class="tri"></span>Hot Water Systems</li>
    <li><span class="tri"></span>Tap &amp; Toilet Repairs</li>
    <li><span class="tri"></span>Stormwater Repairs</li>
    <li><span class="tri"></span>CCTV Drain Inspections</li>
    <li><span class="tri"></span>Gutter &amp; Roof Plumbing</li>
    <li><span class="tri"></span>Preventative Plumbing Maintenance</li>
  </ul>
  <div class="abs tag why-tag">Why Choose VKD Plumbing?</div>
  <ul class="abs tri-list why-list">
    <li><span class="tri"></span>Fully Licensed &amp; Insured</li>
    <li><span class="tri"></span>Upfront Honest Pricing</li>
    <li><span class="tri"></span>Fast Local Service</li>
    <li><span class="tri"></span>Clean &amp; Professional Workmanship</li>
    <li><span class="tri"></span>Trusted by Local Homeowners &amp; Businesses</li>
  </ul>
  <div class="abs reviews-band"></div>
  <svg class="abs reviews-tab" width="262" height="20" viewBox="0 0 262 20"><path d="M0,0 L232,0 L262,20 L0,20 Z" fill="#29bde6"/></svg>
  <div class="abs reviews-tab-text">What Our Customers Say</div>
  <div class="abs rating-source"><span class="name">Fintaro</span><span class="sub">Ratings ★★★★★</span></div>
  <div class="abs quotes">
    <span class="stars">★★★★★</span>
    <p>"Lachlan from VKD Plumbing cleared our blocked<br>drain quickly and professionally. Highly recommend!"</p>
    <span class="stars">★★★★★</span>
    <p>"Prompt, reliable and great service.<br>Will definitely use again."</p>
  </div>
  <div class="abs contact-band">
    <svg class="phone-icon" width="12" height="20" viewBox="0 0 12 20"><rect x="0" y="0" width="12" height="20" rx="3" fill="#29bde6"/><rect x="2.5" y="3" width="7" height="6" fill="#1a75bb"/></svg>
    <svg class="pointer" width="9" height="12" viewBox="0 0 9 12"><path d="M0,0 L0,11 L3,8 L5,12 L7,11 L5,7 L9,7 Z" fill="#f6bf3c"/></svg>
    <div class="need">Need a Plumber?</div>
    <div class="call"><span class="word">Call </span>0491 570 006</div>
    <div class="web">vkdplumbing.com.au</div>
  </div>
  <p class="abs discount">$59 OFF ANY PLUMBING REPAIR<br>(Mention this flyer when booking)</p>
</section>

<!-- Magnet -->
<section class="panel magnet" aria-label="Fridge magnet">
  <svg class="abs magnet-shapes" width="324" height="231" viewBox="0 0 324 231">
    <path d="M0,124 Q110,105 180,165 Q240,215 324,165 L324,231 L0,231 Z" fill="#29bde6"/>
    <path d="M0,140 Q95,128 185,231 L0,231 Z" fill="#ffffff"/>
  </svg>
  <div class="abs mag-need">
    <span class="q">Need a Plumber?</span>
    <div class="call"><span class="word">Call </span>0491 570 006</div>
    <span class="web">vkdplumbing.com.au</span>
  </div>
  <div class="abs mag-tag">OUR SERVICES</div>
  <ul class="abs tri-list mag-list">
    <li><span class="tri"></span>Blocked Drains</li>
    <li><span class="tri"></span>Leak Detection &amp; Repairs</li>
    <li><span class="tri"></span>Hot Water Systems</li>
    <li><span class="tri"></span>Tap &amp; Toilet Repairs</li>
    <li><span class="tri"></span>Stormwater Repairs</li>
    <li><span class="tri"></span>CCTV Drain Inspections</li>
    <li><span class="tri"></span>Gutter &amp; Roof Plumbing</li>
    <li class="two"><span class="tri"></span>Preventative Plumbing<br>Maintenance</li>
  </ul>
  <div class="abs person-magnet" role="img" aria-label="Photo of the plumber Lachlan standing in a navy polo shirt"></div>
  <div class="abs mag-brand"><span class="brand-name">VKD</span><span class="brand-sub">PLUMBING</span></div>
</section>

</body>
</html>
```